unique professional wordpress website design for high end limo rental / car rental company

We need a elegant and professional website (ready to use wordpress theme) for a Car rental / Transport services company. We provide luxury cars on rental and lease. Website needs to be unique, high end and classy and should project the brand name and value proposition. It should not be similar to any existing websites with the same or similar brand name and category. Files should be as a ready to use wordpress 4.7 compatible theme file and should include images and video (stock footage) or links to the stock items used.

Home page should have a full width video background similar to the link below. Something similar can be used.

https://www.videohost-example.com/watch?v=Qz3rT_wmx8P

Menu Structure:
Home (Video background, menu)

Vehicles (banner, two column design with alternate image and content)

Services ( Events, Shuttle Services, Airport Limo, Executive Limo, Point to Point) Seperate page for each sub menu with 2 column content and image

Prices (Drop down selection for start point and end point) also can be selected from map.

Gallery (Video and image gallery - Thumbnail view)

About us : Content and images in alternating blocks

Contact Us : Address, contact details, location map, and Contact us form (Name, email address, Mobile phone, Query / Question) and send button. to be connected to email address later.

Website Footer to have the following (Testimonials single line text moving), Social media icons along with likes / tweets number only, and hyperlink. Contact address, and Newsletter subscription.

Book now Button will lead to the Booking page and payment gateway. Will be done seperately

Header will have Contact numbers, Access email (Button) Book now (Button)

Company : Orvane Limousine
domain : https://www.orvane-example.limo
Sector : Transport solutions, taxi, vehicle rental, chauffer services
Preferred colors : Blue, White, Gold, Black

Files should be compatible with Wordpress 4.7, and should optionally have html/css included along with stock images and video / links.

Target Market(s)

B2B, Transport

Industry/Entity Type

Travel Industry

Font styles to use
Serif
Sans Serif

Requirements
Must have
• Wordpress theme files, HTML/CSS, images and video (links)
Nice to have
• ecommerce page design for cab booking, similar to this:
• https://book.tarvixcoaches-example.com/BookingApp/FastBooking?y
Should not have
• no copy paste or using existing commercial wordpress templates.

```html
<!DOCTYPE html>
<html lang="en">
<head>
<meta charset="utf-8">
<title>Orvane Limousine</title>
<link href="https://fonts.googleapis.com/css2?family=Roboto+Slab:wght@400;700&family=Roboto:wght@400;500;700&display=swap" rel="stylesheet">
<style>
:root{
  --black:#050505;
  --gold:#c9a14a;
  --gold-light:#e2c06e;
  --gold-dark:#ae8535;
  --blue:#1d5fae;
  --sky:#8ecbf6;
  --sky-2:#b5cdee;
  --sky-3:#c8daf3;
  --pale:#eef0f8;
  --grey-panel:#ededf0;
  --footer:#f4f4f6;
  --ink:#1b1b1b;
  --muted:#555;
  --white:#fff;
}
*{box-sizing:border-box;margin:0;padding:0}
html,body{width:1200px;height:3475px;overflow:hidden}
body{position:relative;background:var(--white);font-family:"Roboto",Arial,sans-serif;color:var(--ink)}
.abs{position:absolute}
.slab{font-family:"Roboto Slab",Georgia,serif}
.section-title{position:absolute;left:0;width:1200px;text-align:center;font-family:"Roboto Slab",Georgia,serif;font-size:34px;font-weight:400;color:var(--ink)}
.btn-gold{position:absolute;display:flex;align-items:center;justify-content:center;background:linear-gradient(180deg,var(--gold-light),var(--gold-dark));color:var(--white);font-size:14px;font-weight:500;border-radius:2px}
.photo{position:absolute}

/* hero */
.hero{left:0;top:0;width:1200px;height:598px;background:linear-gradient(180deg,#3a4a5a 0%,#6b6f6a 22%,#7d6a45 40%,#4d3e26 60%,#2a2216 100%)}
.topbar{left:100px;top:0;width:1000px;height:123px;background:var(--black)}
.brand{left:127px;top:40px;display:flex;align-items:center;gap:10px;color:var(--gold);font-family:"Roboto Slab",Georgia,serif;font-size:24px}
.brand .dot{width:14px;height:14px;border-radius:50%;background:var(--gold)}
.contact-item{top:14px;display:flex;align-items:center;gap:10px;color:var(--white);font-size:13px;white-space:nowrap}
.ring{width:34px;height:34px;flex:none;border:1.5px solid #aaa;border-radius:50%;display:flex;align-items:center;justify-content:center}
.nav{left:419px;top:76px;display:flex;color:var(--white);font-size:15px}
.nav span{padding:7px 14px}
.nav .active{background:var(--gold);color:var(--black)}
.play{left:561px;top:327px;width:74px;height:74px;border:2px solid var(--white);border-radius:50%;display:flex;align-items:center;justify-content:center}
.watch{left:500px;top:408px;width:200px;text-align:center;color:var(--white);font-size:12px}

/* vehicles */
.veh-panel{left:600px;top:672px;width:600px;height:347px;background:var(--grey-panel)}
.veh-name{font-family:"Roboto Slab",Georgia,serif;font-size:34px;color:var(--ink)}
.veh-text{font-size:11px;font-style:italic;line-height:20px;color:var(--ink)}
.arrow-box{width:28px;height:28px;background:var(--white);display:flex;align-items:center;justify-content:center;box-shadow:0 0 3px rgba(0,0,0,.2)}
.car{border-radius:6px}

/* services */
.service-tile{top:1114px;width:247px;height:144px}
.service-label{top:1263px;width:247px;text-align:center;font-family:"Roboto Slab",Georgia,serif;font-size:20px}
.slide-arrow{width:24px;height:24px;border-radius:50%;background:rgba(255,255,255,.9);display:flex;align-items:center;justify-content:center}

/* prices */
.prices-bg{left:0;top:1367px;width:1200px;height:509px;background:var(--pale)}
.select{left:496px;top:1446px;width:204px;height:26px;background:var(--white);border:1px solid #ddd;font-size:11px;color:#666;padding:5px 14px;display:flex;justify-content:space-between}
.price-card{top:1503px;width:226px;height:306px;text-align:center}
.price-card .name{margin-top:28px;font-family:"Roboto Slab",Georgia,serif;font-size:34px}
.price-card .type{font-family:"Roboto Slab",Georgia,serif;font-size:16px;margin-top:2px}
.price-card .amount{font-family:"Roboto Slab",Georgia,serif;font-size:56px;margin-top:8px;line-height:64px}
.price-card ul{list-style:none;font-size:12px;line-height:23px;margin-top:14px}

/* about */
.about-text{left:192px;top:2364px;width:816px;text-align:center;font-size:11.5px;line-height:22px}

/* contact */
.contact-bg{left:0;top:2555px;width:1200px;height:410px;background:var(--pale)}
.label-head{font-size:20px;color:var(--ink)}
.info{font-size:12px;color:var(--ink);display:flex;gap:10px;align-items:center;white-space:nowrap}
.map{left:139px;top:2738px;width:456px;height:204px;background:linear-gradient(135deg,#cfe3c4,#e9eadf 45%,#a9cdee 70%,#8fbde6)}
.field{left:639px;width:406px;height:40px;background:var(--white);border:1px solid #dcdcdc;font-size:11px;color:#666;padding:11px 16px}

/* newsletter */
.news{left:0;top:2965px;width:1200px;height:132px;background:var(--blue)}
.news-title{left:181px;top:3012px;color:var(--white);font-family:"Roboto Slab",Georgia,serif;font-size:28px}
.news-input{left:507px;top:3009px;width:304px;height:44px;background:var(--white);font-size:11px;color:#666;padding:15px 24px}

/* footer */
.footer-bg{left:0;top:3208px;width:1200px;height:267px;background:var(--footer)}
.testimonials{left:100px;top:3218px;width:1000px;height:51px;background:var(--gold);display:flex;align-items:center;color:var(--white)}
.testimonials .tag{padding:0 30px;font-family:"Roboto Slab",Georgia,serif;font-size:20px}
.testimonials .quote{font-size:11px}
.footer-nav{left:0;top:3307px;width:1200px;display:flex;justify-content:center;gap:34px;font-size:15px;color:var(--ink)}
.social{top:3344px;width:26px;height:26px;border-radius:50%}
.copyright{left:0;top:3422px;width:1200px;text-align:center;font-size:11px;color:#555}
</style>
</head>
<body>

<!-- hero -->
<div class="abs hero" role="img" aria-label="Video still of a coastal road curving along a cliff at dusk"></div>
<div class="abs topbar"></div>
<div class="abs brand"><span class="dot"></span>ORVANE</div>

<div class="abs contact-item" style="left:566px">
  <span class="ring"><svg width="16" height="16" viewBox="0 0 24 24"><path fill="#fff" d="M6.6 10.8a15 15 0 0 0 6.6 6.6l2.2-2.2c.3-.3.7-.4 1-.2 1.1.4 2.3.6 3.6.6.6 0 1 .4 1 1V20c0 .6-.4 1-1 1A17 17 0 0 1 3 4c0-.6.4-1 1-1h3.5c.6 0 1 .4 1 1 0 1.3.2 2.5.6 3.6.1.3 0 .7-.2 1z"/></svg></span>1-800 555 0142
</div>
<div class="abs contact-item" style="left:714px">
  <span class="ring"><svg width="16" height="16" viewBox="0 0 24 24"><rect x="3" y="6" width="18" height="12" fill="none" stroke="#fff" stroke-width="2"/><path d="M3 6l9 7 9-7" fill="none" stroke="#fff" stroke-width="2"/></svg></span>info@orvane-example.limo
</div>
<div class="abs contact-item" style="left:958px">
  <span class="ring"><svg width="16" height="16" viewBox="0 0 24 24"><path d="M6 3h12v18l-6-5-6 5z" fill="none" stroke="#fff" stroke-width="2"/></svg></span>Book Now
</div>

<nav class="abs nav">
  <span class="active">Home</span><span>Vehicles</span><span>Services</span><span>Prices</span><span>Gallery</span><span>About Us</span><span>Contact Us</span>
</nav>

<div class="abs play"><svg width="26" height="28" viewBox="0 0 26 28"><path d="M4 2l20 12L4 26z" fill="#fff"/></svg></div>
<div class="abs watch">Watch this video</div>

<!-- vehicles -->
<h2 class="section-title" style="top:618px">Vehicles</h2>

<div class="photo car" style="left:20px;top:760px;width:335px;height:200px;background:linear-gradient(160deg,#8a7a6c 0%,#5a4b3e 45%,#3b322b 100%)" role="img" aria-label="Dark brown estate car, three-quarter view"></div>
<div class="abs veh-name" style="left:380px;top:738px">Limo</div>
<p class="abs veh-text" style="left:380px;top:796px;width:182px">Neque porro quisquam est qui dolorem ipsum quia dolor sit amet, consectetur, adipisci velit...</p>
<div class="btn-gold" style="left:380px;top:873px;width:118px;height:40px">Book Now</div>

<div class="abs veh-panel"></div>
<div class="abs arrow-box" style="left:570px;top:784px"><svg width="10" height="10" viewBox="0 0 10 10"><path d="M7 1L3 5l4 4" fill="none" stroke="#333" stroke-width="1.6"/></svg></div>
<div class="abs arrow-box" style="left:600px;top:812px"><svg width="10" height="10" viewBox="0 0 10 10"><path d="M3 1l4 4-4 4" fill="none" stroke="#333" stroke-width="1.6"/></svg></div>
<div class="abs veh-name" style="left:660px;top:720px">Orvane Limousine</div>
<p class="abs veh-text" style="left:660px;top:778px;width:440px">We are working hard to create a better experience for you. So watch this space, as we unravel the best in travel solutions</p>
<div class="btn-gold" style="left:660px;top:841px;width:121px;height:38px">Book Now</div>
<div class="photo car" style="left:960px;top:850px;width:220px;height:135px;background:linear-gradient(160deg,#55555c 0%,#2a2a2e 45%,#141416 100%)" role="img" aria-label="Black luxury sedan, front three-quarter view"></div>

<!-- services -->
<h2 class="section-title" style="top:1050px">Services</h2>
<div class="photo service-tile" style="left:100px;background:linear-gradient(135deg,#2b2320,#6a5548 55%,#1d1715)" role="img" aria-label="Couple in evening wear stepping out of a limousine"></div>
<div class="photo service-tile" style="left:351px;background:linear-gradient(135deg,#d6dde2,#6a6e73 50%,#1e1f22)" role="img" aria-label="Chauffeur in cap at the wheel"></div>
<div class="photo service-tile" style="left:602px;background:linear-gradient(180deg,#c9d8e6,#e9eef3 50%,#9aa3a9)" role="img" aria-label="Private jet and limousine on an airport apron"></div>
<div class="photo service-tile" style="left:853px;background:linear-gradient(135deg,#3a3431,#7b6d63 55%,#2a2522)" role="img" aria-label="Business passenger on a phone in the back seat"></div>
<div class="abs slide-arrow" style="left:102px;top:1174px"><svg width="10" height="10" viewBox="0 0 10 10"><path d="M7 1L3 5l4 4" fill="none" stroke="#333" stroke-width="1.6"/></svg></div>
<div class="abs slide-arrow" style="left:1074px;top:1174px"><svg width="10" height="10" viewBox="0 0 10 10"><path d="M3 1l4 4-4 4" fill="none" stroke="#333" stroke-width="1.6"/></svg></div>
<div class="abs service-label" style="left:100px">Events</div>
<div class="abs service-label" style="left:351px">Shuttle Services</div>
<div class="abs service-label" style="left:602px">Airport Limo</div>
<div class="abs service-label" style="left:853px">Executive Limo</div>

<!-- prices -->
<div class="abs prices-bg"></div>
<h2 class="section-title" style="top:1384px">Prices</h2>
<div class="abs select"><span>Premium</span><span>▾</span></div>

<div class="abs price-card" style="left:255px;background:var(--sky)">
  <div class="name">Limo</div><div class="type">Type 1</div><div class="amount">$140</div>
  <ul><li>Various versions</li><li>Lorem Ipsum</li><li>Finibus Bonorum</li><li>Malorum</li></ul>
</div>
<div class="abs price-card" style="left:487px;background:var(--sky-2)">
  <div class="name">Limo</div><div class="type">Type 2</div><div class="amount">$240</div>
  <ul><li>Various versions</li><li>Lorem Ipsum</li><li>Finibus Bonorum</li><li>Malorum</li></ul>
</div>
<div class="abs price-card" style="left:720px;background:var(--sky-3)">
  <div class="name">Limo</div><div class="type">Type 3</div><div class="amount">$440</div>
  <ul><li>Various versions</li><li>Lorem Ipsum</li><li>Finibus Bonorum</li><li>Malorum</li></ul>
</div>
<div class="btn-gold" style="left:308px;top:1793px;width:120px;height:35px">Book Now</div>
<div class="btn-gold" style="left:540px;top:1793px;width:120px;height:35px">Book Now</div>
<div class="btn-gold" style="left:773px;top:1793px;width:120px;height:35px">Book Now</div>

<!-- gallery -->
<h2 class="section-title" style="top:1910px">Gallery</h2>
<div class="photo" style="left:100px;top:1969px;width:486px;height:290px;background:linear-gradient(135deg,#1a2440,#4a3a3a 45%,#b87a3a 75%,#1a1a2a)" role="img" aria-label="Video still of a couple by a limousine at night"></div>
<div class="abs play" style="left:306px;top:2078px;width:66px;height:66px;background:rgba(0,0,0,.35)"><svg width="22" height="24" viewBox="0 0 26 28"><path d="M4 2l20 12L4 26z" fill="#fff"/></svg></div>
<div class="photo" style="left:600px;top:1969px;width:243px;height:139px;background:linear-gradient(135deg,#1c2a44,#5a6e8c 55%,#1a2030)" role="img" aria-label="Wedding couple in a limousine interior"></div>
<div class="photo" style="left:855px;top:1969px;width:245px;height:139px;background:linear-gradient(135deg,#2a3440,#1a1f26 55%,#6b7684)" role="img" aria-label="Classic dark limousine front"></div>
<div class="photo" style="left:600px;top:2122px;width:243px;height:137px;background:linear-gradient(135deg,#3a3634,#8a7f78 55%,#2a2624)" role="img" aria-label="Businessman working on a laptop in a car"></div>
<div class="photo" style="left:855px;top:2122px;width:245px;height:137px;background:linear-gradient(180deg,#9a9a9a,#6e6e6e 55%,#a83a30 80%,#505050)" role="img" aria-label="Red vintage car on a city street"></div>

<!-- about -->
<h2 class="section-title" style="top:2294px">About us</h2>
<p class="abs about-text">Nor again is there anyone who loves or pursues or desires to obtain pain of itself, because it is pain, but because occasionally circumstances occur in which toil and pain can procure him some great pleasure. Et harum quidem rerum facilis est et expedita distinctio. Nam libero tempore, cum soluta nobis est eligendi optio cumque nihil impedit quo minus id quod maxime placeat facere possimus, omnis voluptas assumenda est, omnis dolor repellendus. Temporibus autem quibusdam et aut officiis debitis aut rerum</p>
<div class="btn-gold" style="left:540px;top:2476px;width:120px;height:38px">Read more</div>

<!-- contact -->
<div class="abs contact-bg"></div>
<div class="abs label-head" style="left:139px;top:2592px">ADDRESS</div>
<div class="abs info" style="left:139px;top:2638px">
  <svg width="12" height="12" viewBox="0 0 24 24"><path fill="#333" d="M6.6 10.8a15 15 0 0 0 6.6 6.6l2.2-2.2c.3-.3.7-.4 1-.2 1.1.4 2.3.6 3.6.6.6 0 1 .4 1 1V20c0 .6-.4 1-1 1A17 17 0 0 1 3 4c0-.6.4-1 1-1h3.5c.6 0 1 .4 1 1 0 1.3.2 2.5.6 3.6.1.3 0 .7-.2 1z"/></svg>Phone : 1-800 555 0187
</div>
<div class="abs info" style="left:139px;top:2668px">
  <svg width="12" height="12" viewBox="0 0 24 24"><rect x="3" y="6" width="18" height="12" fill="none" stroke="#333" stroke-width="2"/><path d="M3 6l9 7 9-7" fill="none" stroke="#333" stroke-width="2"/></svg>Email : info@orvane-example.limo
</div>
<div class="abs info" style="left:387px;top:2638px">
  <svg width="12" height="14" viewBox="0 0 24 28"><path fill="#333" d="M12 0a9 9 0 0 0-9 9c0 7 9 19 9 19s9-12 9-19a9 9 0 0 0-9-9zm0 13a4 4 0 1 1 0-8 4 4 0 0 1 0 8z"/></svg>Address : Orvane Offices
</div>
<div class="abs info" style="left:417px;top:2668px">Level 12, 48 Harbour Lane</div>
<div class="abs info" style="left:417px;top:2698px">Sydney NSW 2000</div>
<div class="abs map" role="img" aria-label="Location map of the Sydney harbour area"></div>

<div class="abs label-head" style="left:639px;top:2585px">CONTACT US</div>
<div class="abs field" style="top:2636px">Name</div>
<div class="abs field" style="top:2694px">Email</div>
<div class="abs field" style="top:2754px">Phone Number</div>
<div class="abs field" style="top:2812px;height:84px">Message</div>
<div class="btn-gold" style="left:642px;top:2910px;width:106px;height:32px;font-size:12px">SEND</div>

<!-- newsletter -->
<div class="abs news"></div>
<div class="abs news-title">Newsletter Subscribe</div>
<div class="abs news-input">EMAIL ADDRESS</div>
<div class="btn-gold" style="left:811px;top:3009px;width:136px;height:44px;font-size:12px">SUBSCRIBE</div>

<!-- brand strip -->
<div class="abs" style="left:140px;top:3112px;width:44px;height:44px;border-radius:50%;background:var(--gold)"></div>
<div class="abs slab" style="left:220px;top:3118px;font-size:26px;color:var(--gold)">Orvane Limousine</div>
<div class="abs" style="left:220px;top:3158px;font-size:12px;color:var(--muted)">Sint occaecati cupiditate non provident, similique sunt in culpa qui officia deserunt mollitia animi,</div>
<div class="btn-gold" style="left:813px;top:3137px;width:123px;height:34px">Book Now</div>

<!-- footer -->
<div class="abs footer-bg"></div>
<div class="abs testimonials">
  <span class="tag">TESTIMONIALS</span>
  <span class="quote">Et harum quidem rerum facilis est et expedita distinctio. Nam libero tempore, cum soluta nobis est eligendi optio cumque nihil impedit</span>
</div>
<div class="abs footer-nav">
  <span>Home</span><span>Vehicles</span><span>Services</span><span>Prices</span><span>Gallery</span><span>About Us</span><span>Contact Us</span>
</div>
<div class="abs social" style="left:535px;background:#2d4a8a"></div>
<div class="abs social" style="left:567px;background:#2aa3e0"></div>
<div class="abs social" style="left:599px;background:#d8342a"></div>
<div class="abs social" style="left:631px;background:#b08a4a"></div>
<div class="abs copyright">Copyrights © 2017, www.orvane-example.limo. All Rights Reserved.</div>

</body>
</html>
```